Football field themed poster-game

I'm looking for a 22" x 29" size poster with a minimum of 300dpi, max of 300mb. File format can be jpg, gif, tiff or bmp. Would like the field portion of the poster to appear like a real grass football field. The field will need makers for each yard. I've added an addition simple clip art that shows another way for yard lines as well.The rest of the layout I would like similar, but made to look more professional. Wording should be the same as in the given draft and located in the same area or close to that area on the poster. The style is open, but should be a little minimalist in nature. Design work has to be original and cannot be taken from trademarked or copyrighted items.
Updates

Project Deadline Extended
Reason: I have 2 or 3 designs that really standout, but I would like to see just a few more.

Target Market(s)

Football fans

Font styles to use
Sans Serif

Colors

Designer to choose colors to be used in the design.

Requirements
Must have
• The design must have the same similar layout as the file I have submitted with the contest. The football field needs to be made to look like a real field with turf. boarders would be nice and a modern look.
Should not have
• hard to read fonts, changes to the major overall layout of poster.

```html
<!DOCTYPE html>
<html lang="en">
<head>
<meta charset="utf-8">
<title>Turf Cup – Football Field Game Poster</title>
<link href="https://fonts.googleapis.com/css2?family=Roboto+Condensed:wght@500;700&family=Saira:wght@700;800&display=swap" rel="stylesheet">
<style>
  :root {
    --turf-dark: #2c7424;
    --turf-mid: #3b8a2c;
    --turf-light: #4a9a36;
    --chalk: #ffffff;
    --home: #c8582a;
    --home-light: #d86a35;
    --visitors: #2b4fa0;
    --visitors-light: #3560b8;
    --score-red: #e2262b;
    --score-blue: #2e3496;
    --ink: #111111;
    --frame-blue: #2e3a96;
  }
  html, body {
    margin: 0;
    padding: 0;
    width: 1200px;
    height: 909px;
    overflow: hidden;
    background: var(--turf-mid);
  }
  .poster {
    display: block;
    width: 1200px;
    height: 909px;
  }
  .yard-number {
    font-family: "Roboto Condensed", sans-serif;
    font-weight: 500;
    font-size: 42px;
    fill: var(--chalk);
  }
  .endzone-label {
    font-family: "Saira", sans-serif;
    font-weight: 800;
    font-size: 50px;
    fill: var(--chalk);
    letter-spacing: 1px;
  }
  .score-label {
    font-family: "Saira", sans-serif;
    font-weight: 800;
    font-size: 34px;
    fill: var(--ink);
  }
  .game-title {
    font-family: "Saira", sans-serif;
    font-weight: 800;
    font-size: 50px;
    fill: var(--score-red);
  }
</style>
</head>
<body>
<svg class="poster" viewBox="0 0 1074 814" width="1200" height="909" xmlns="http://www.w3.org/2000/svg">
  <defs>
    <linearGradient id="turf-shade" x1="0" y1="0" x2="0" y2="1">
      <stop offset="0" stop-color="var(--turf-light)"/>
      <stop offset="0.5" stop-color="var(--turf-mid)"/>
      <stop offset="1" stop-color="var(--turf-dark)"/>
    </linearGradient>
    <linearGradient id="home-fill" x1="0" y1="0" x2="1" y2="1">
      <stop offset="0" stop-color="var(--home-light)"/>
      <stop offset="1" stop-color="var(--home)"/>
    </linearGradient>
    <linearGradient id="visitors-fill" x1="0" y1="0" x2="1" y2="1">
      <stop offset="0" stop-color="var(--visitors-light)"/>
      <stop offset="1" stop-color="var(--visitors)"/>
    </linearGradient>
    <pattern id="mow-stripes" patternUnits="userSpaceOnUse" x="120" y="0" width="83.7" height="10">
      <rect width="41.85" height="10" fill="#000" opacity="0.06"/>
    </pattern>
    <pattern id="yard-lines" patternUnits="userSpaceOnUse" x="118.5" y="0" width="41.85" height="10">
      <rect x="0" width="3" height="10" fill="var(--chalk)"/>
    </pattern>
    <pattern id="hash-ticks" patternUnits="userSpaceOnUse" x="118.5" y="0" width="41.85" height="20">
      <rect x="8.4" width="1.8" height="20" fill="var(--chalk)"/>
      <rect x="16.8" width="1.8" height="20" fill="var(--chalk)"/>
      <rect x="25.2" width="1.8" height="20" fill="var(--chalk)"/>
      <rect x="33.6" width="1.8" height="20" fill="var(--chalk)"/>
    </pattern>
  </defs>

  <!-- turf background -->
  <rect class="turf" width="1074" height="814" fill="url(#turf-shade)"/>

  <!-- playing field -->
  <g class="field">
    <rect x="22" y="22" width="1032" height="516" fill="none" stroke="var(--chalk)" stroke-width="4"/>
    <rect x="120" y="33" width="837" height="500" fill="url(#mow-stripes)"/>

    <rect class="endzone endzone--home" x="30" y="33" width="88" height="500" fill="url(#home-fill)"/>
    <rect class="endzone endzone--visitors" x="957" y="33" width="88" height="500" fill="url(#visitors-fill)"/>

    <rect class="yard-lines" x="118.5" y="33" width="841" height="500" fill="url(#yard-lines)"/>
    <rect class="hash-marks" x="118.5" y="40" width="838" height="15" fill="url(#hash-ticks)"/>
    <rect class="hash-marks" x="118.5" y="491" width="838" height="15" fill="url(#hash-ticks)"/>

    <circle class="midfield-emblem" cx="537" cy="270" r="70" fill="#6fc050" opacity="0.18" role="img" aria-label="Faint football helmet emblem at midfield"/>

    <text class="endzone-label" transform="translate(74 283) rotate(90)" text-anchor="middle" dominant-baseline="central">HOME</text>
    <text class="endzone-label" transform="translate(1001 283) rotate(-90)" text-anchor="middle" dominant-baseline="central">VISITORS</text>

    <g class="yard-numbers yard-numbers--bottom">
      <text class="yard-number" x="200" y="454" text-anchor="end">1</text><text class="yard-number" x="208" y="454">0</text>
      <text class="yard-number" x="284" y="454" text-anchor="end">2</text><text class="yard-number" x="292" y="454">0</text>
      <text class="yard-number" x="368" y="454" text-anchor="end">3</text><text class="yard-number" x="376" y="454">0</text>
      <text class="yard-number" x="451" y="454" text-anchor="end">4</text><text class="yard-number" x="459" y="454">0</text>
      <text class="yard-number" x="535" y="454" text-anchor="end">5</text><text class="yard-number" x="543" y="454">0</text>
      <text class="yard-number" x="619" y="454" text-anchor="end">4</text><text class="yard-number" x="627" y="454">0</text>
      <text class="yard-number" x="702" y="454" text-anchor="end">3</text><text class="yard-number" x="710" y="454">0</text>
      <text class="yard-number" x="786" y="454" text-anchor="end">2</text><text class="yard-number" x="794" y="454">0</text>
      <text class="yard-number" x="870" y="454" text-anchor="end">1</text><text class="yard-number" x="878" y="454">0</text>
    </g>
    <g class="yard-numbers yard-numbers--top" transform="rotate(180 537 285)">
      <text class="yard-number" x="200" y="454" text-anchor="end">1</text><text class="yard-number" x="208" y="454">0</text>
      <text class="yard-number" x="284" y="454" text-anchor="end">2</text><text class="yard-number" x="292" y="454">0</text>
      <text class="yard-number" x="368" y="454" text-anchor="end">3</text><text class="yard-number" x="376" y="454">0</text>
      <text class="yard-number" x="451" y="454" text-anchor="end">4</text><text class="yard-number" x="459" y="454">0</text>
      <text class="yard-number" x="535" y="454" text-anchor="end">5</text><text class="yard-number" x="543" y="454">0</text>
      <text class="yard-number" x="619" y="454" text-anchor="end">4</text><text class="yard-number" x="627" y="454">0</text>
      <text class="yard-number" x="702" y="454" text-anchor="end">3</text><text class="yard-number" x="710" y="454">0</text>
      <text class="yard-number" x="786" y="454" text-anchor="end">2</text><text class="yard-number" x="794" y="454">0</text>
      <text class="yard-number" x="870" y="454" text-anchor="end">1</text><text class="yard-number" x="878" y="454">0</text>
    </g>
  </g>

  <!-- scoreboard -->
  <g class="scoreboard">
    <rect x="22" y="549" width="1032" height="249" fill="none" stroke="var(--chalk)" stroke-width="4"/>

    <g class="score-dial score-dial--home">
      <circle cx="167" cy="673" r="103" fill="var(--chalk)"/>
      <circle cx="167" cy="673" r="95" fill="var(--score-red)"/>
      <rect x="107" y="612" width="121" height="121" fill="var(--chalk)" stroke="var(--ink)" stroke-width="4"/>
    </g>
    <g class="score-tag score-tag--home">
      <rect x="287" y="586" width="53" height="170" rx="9" fill="var(--chalk)"/>
      <text class="score-label" transform="translate(313.5 671) rotate(90)" text-anchor="middle" dominant-baseline="central">SCORE</text>
    </g>

    <g class="game-badge">
      <rect x="392" y="583" width="290" height="177" rx="6" fill="var(--chalk)" stroke="var(--frame-blue)" stroke-width="2.5"/>
      <text class="game-title" x="440" y="652">TURF</text>
      <circle cx="455" cy="708" r="20" fill="none" stroke="var(--score-red)" stroke-width="3"/>
      <text class="game-title" x="500" y="728">CUP</text>
    </g>

    <g class="score-tag score-tag--visitors">
      <rect x="731" y="586" width="53" height="170" rx="9" fill="var(--chalk)"/>
      <text class="score-label" transform="translate(757.5 671) rotate(-90)" text-anchor="middle" dominant-baseline="central">SCORE</text>
    </g>
    <g class="score-dial score-dial--visitors">
      <circle cx="903" cy="673" r="103" fill="var(--chalk)"/>
      <circle cx="903" cy="673" r="95" fill="var(--score-blue)"/>
      <rect x="843" y="612" width="121" height="121" fill="var(--chalk)" stroke="var(--ink)" stroke-width="4"/>
    </g>
  </g>
</svg>
</body>
</html>
```